Infographic for Local Fence Company

I want to create an infographic for our fence installation business. The infographic will display helpful information that shows the fence installation process from start to finish. It will detail information starting from how to get an estimate (virtual by email, facebook message, phone or in person) and then some common things that happen during the install (we contact 627 to mark for public lines, but they do not mark private lines like sprinklers) and then towards the end the customer will see their brand new fence installed. It may be good to show a little bit during the quoting process how we differ from other companies, offering a lifetime warranty on workmanship and free gate alignments for life. Our website is www.MyBrambleyardPosts.com and company info will be shown there -- our competitors website is https://www.toplinepicketworks.com/fence-services/fence-video-tutorials/ and we like the way their video tutorials explain some of the similar things we want mentioned.

Target Market(s)

Potential Customers Ages 24 - 60

Industry/Entity Type

Fence Installation in Charlotte NC area (USA)

Font styles to use
Sans Serif

Colors
0094D4
00A9DD
6FCCEA
C7EBF8
E9F6FB

Requirements
Must have
• Drawn characters showing the fence process
Nice to have
• I would like to see an infographic that displays someone being pensive about what company to choose, choosing our company and then go through the process of having the fence work done in a light and happy feeling
Should not have
• other competitors names

```html
<!DOCTYPE html>
<html lang="en">
<head>
<meta charset="utf-8">
<title>Brambleyard Posts – Fence Installation Guide</title>
<link rel="stylesheet" href="https://fonts.googleapis.com/css2?family=Poppins:wght@500;600;700&display=swap">
<style>
  :root {
    --brand-blue: #3d86c6;
    --ink: #111111;
    --slate: #4a5866;
    --panel: #f0f0f0;
    --sun: #fdb515;
    --sun-deep: #fca60f;
    --pill: #c6c6c6;
    --green: #3cb54a;
    --line-blue: #2ba6df;
    --line-orange: #e8893a;
    --badge-blue: #3d86c6;
    --badge-orange: #e8923a;
    --badge-brown: #5a3e2f;
    --hex-tint: #f1e1df;
    --white: #ffffff;
  }
  * { box-sizing: border-box; margin: 0; padding: 0; }
  html, body { width: 1200px; height: 2424px; overflow: hidden; background: var(--white); }
  body { font-family: "Poppins", sans-serif; position: relative; }
  .abs { position: absolute; }

  /* header */
  .brand-mark { left: 55px; top: 42px; width: 88px; height: 116px; background: #5a3e2f; }
  .brand-name { left: 163px; top: 46px; font-size: 34px; font-weight: 700; color: var(--brand-blue); line-height: 1; }
  .brand-phone { left: 163px; top: 92px; font-size: 33px; font-weight: 700; color: var(--ink); line-height: 1; }
  .brand-tagline { left: 163px; top: 137px; font-size: 11px; font-weight: 600; color: var(--ink); }
  .hero-banner { left: 524px; top: 40px; width: 676px; height: 118px; }
  .hero-banner-text { left: 623px; top: 64px; font-size: 26px; font-weight: 600; color: var(--white); line-height: 1.3; }

  /* body panel */
  .panel { left: 4px; top: 185px; width: 1194px; height: 2239px; background: var(--panel); }
  .contact-title { left: 0; top: 238px; width: 1200px; text-align: center; font-size: 36px; font-weight: 600; color: var(--slate); }

  .contact-band { left: 3px; top: 327px; width: 1197px; height: 330px; background: var(--sun); border-top-right-radius: 130px; }
  .house-art { left: 405px; top: 388px; width: 405px; height: 277px; background: linear-gradient(180deg, #b9272c 0%, #e8e8e8 55%, #c62a31 100%); }
  .icon-dot { width: 98px; height: 98px; border-radius: 50%; background: var(--ink); display: flex; align-items: center; justify-content: center; }

  .rule { height: 10px; border-radius: 5px; }

  .call-pill { left: 108px; top: 765px; width: 559px; height: 117px; background: var(--pill); border-radius: 59px; }
  .call-circle { left: 108px; top: 755px; width: 140px; height: 140px; border-radius: 50%; background: var(--ink); display: flex; align-items: center; justify-content: center; }
  .call-word { left: 277px; top: 776px; font-size: 48px; font-weight: 600; color: var(--ink); line-height: 1; }
  .call-sub { left: 278px; top: 830px; font-size: 28px; font-weight: 600; color: var(--ink); line-height: 1; }
  .call-number { left: 468px; top: 770px; font-size: 96px; font-weight: 700; color: var(--ink); line-height: 1; letter-spacing: -3px; }
  .idea-art { left: 885px; top: 793px; width: 118px; height: 262px; background: linear-gradient(180deg, #fdc20f 0%, #f07c1f 50%, #2a5ba8 100%); border-radius: 50px 50px 10px 10px; }

  .select-band { left: 4px; top: 946px; width: 1037px; height: 117px; }
  .select-text { left: 130px; top: 984px; font-size: 37px; font-weight: 700; color: var(--white); }

  .fence-title { font-size: 44px; font-weight: 600; color: var(--slate); line-height: 1; }
  .badge-num { font-size: 96px; font-weight: 700; color: var(--white); line-height: 1; }
  .wood-art { left: 652px; top: 1192px; width: 455px; height: 186px; background: linear-gradient(180deg, #e9a562 0%, #b9713a 100%); }
  .gate-art { left: 122px; top: 1545px; width: 472px; height: 260px; background: linear-gradient(180deg, #6f6f6f 0%, #3b3b3b 100%); }
  .picket-art { left: 378px; top: 2118px; width: 482px; height: 147px; background: linear-gradient(180deg, #a0643a 0%, #7a4726 100%); }
</style>
</head>
<body>

<header>
  <div class="abs brand-mark"></div>
  <div class="abs brand-name">Brambleyard Posts</div>
  <div class="abs brand-phone">555-014-2290</div>
  <div class="abs brand-tagline">“Because Good Fences Make Good Neighbors”</div>
  <svg class="abs hero-banner" viewBox="0 0 676 118"><polygon points="58,0 676,0 676,118 0,118" fill="var(--brand-blue)"/></svg>
  <div class="abs hero-banner-text">Start to Finish Detail Information<br>about fence installation</div>
</header>

<main>
  <div class="abs panel"></div>
  <h2 class="abs contact-title">CONTACT US FOR DETAIL</h2>

  <section>
    <div class="abs contact-band"></div>
    <div class="abs house-art" role="img" aria-label="Illustration of a house with a red roof and garage"></div>

    <div class="abs icon-dot" style="left:303px;top:318px;" aria-label="Message"></div>
    <div class="abs icon-dot" style="left:197px;top:442px;" aria-label="Email">
      <svg width="46" height="34" viewBox="0 0 46 34"><rect x="3" y="3" width="40" height="28" rx="2" fill="none" stroke="#fff" stroke-width="5"/><polyline points="4,5 23,20 42,5" fill="none" stroke="#fff" stroke-width="5" stroke-linejoin="round"/></svg>
    </div>
    <div class="abs icon-dot" style="left:803px;top:318px;" aria-label="Phone">
      <svg width="42" height="42" viewBox="0 0 24 24"><path fill="#fff" d="M6.6 10.8a15 15 0 0 0 6.6 6.6l2.2-2.2a1 1 0 0 1 1-.25 11.4 11.4 0 0 0 3.6.57 1 1 0 0 1 1 1V20a1 1 0 0 1-1 1A17 17 0 0 1 3 4a1 1 0 0 1 1-1h3.5a1 1 0 0 1 1 1c0 1.25.2 2.45.57 3.57a1 1 0 0 1-.25 1z"/></svg>
    </div>
    <div class="abs icon-dot" style="left:903px;top:449px;" aria-label="In person">
      <svg width="40" height="42" viewBox="0 0 40 42"><circle cx="20" cy="12" r="9" fill="none" stroke="#fff" stroke-width="4"/><path d="M4 40c0-10 7-15 16-15s16 5 16 15" fill="none" stroke="#fff" stroke-width="4" stroke-linecap="round"/></svg>
    </div>

    <div class="abs rule" style="left:373px;top:688px;width:463px;background:var(--brand-blue);"></div>
    <div class="abs" style="left:405px;top:712px;width:431px;height:4px;background:var(--line-orange);"></div>
  </section>

  <section>
    <div class="abs call-pill"></div>
    <div class="abs call-circle">
      <svg width="62" height="62" viewBox="0 0 24 24"><path fill="#fff" d="M6.6 10.8a15 15 0 0 0 6.6 6.6l2.2-2.2a1 1 0 0 1 1-.25 11.4 11.4 0 0 0 3.6.57 1 1 0 0 1 1 1V20a1 1 0 0 1-1 1A17 17 0 0 1 3 4a1 1 0 0 1 1-1h3.5a1 1 0 0 1 1 1c0 1.25.2 2.45.57 3.57a1 1 0 0 1-.25 1z"/></svg>
    </div>
    <div class="abs call-word">Call</div>
    <div class="abs call-sub">public line</div>
    <div class="abs call-number">627</div>
    <div class="abs idea-art" role="img" aria-label="Illustration of a person holding up a glowing lightbulb"></div>
  </section>

  <section>
    <svg class="abs select-band" viewBox="0 0 1037 117"><polygon points="0,0 960,0 1037,117 0,117" fill="var(--green)"/></svg>
    <h2 class="abs select-text">YOU SELECT YOUR FENCE CHOICE</h2>
    <svg class="abs" style="left:134px;top:1073px;" width="326" height="24" viewBox="0 0 326 24">
      <polygon points="0,0 326,0 318,10 0,10" fill="var(--line-blue)"/>
      <polygon points="0,20 136,20 132,24 0,24" fill="var(--line-orange)"/>
    </svg>
  </section>

  <!-- soft hexagons -->
  <svg class="abs" style="left:0;top:1150px;" width="1200" height="1200" viewBox="0 1150 1200 1200">
    <g fill="var(--hex-tint)">
      <polygon points="80,1178 178,1178 222,1264 178,1350 80,1350 37,1264"/>
      <polygon points="580,1281 614,1281 632,1310 614,1339 580,1339 564,1310"/>
      <polygon points="1118,1281 1152,1281 1166,1310 1152,1339 1118,1339 1102,1310"/>
      <polygon points="990,1505 1073,1505 1116,1578 1073,1650 990,1650 948,1578"/>
      <polygon points="680,1582 720,1582 740,1616 720,1651 680,1651 660,1616"/>
      <polygon points="273,1788 302,1788 320,1818 302,1848 273,1848 258,1818"/>
      <polygon points="812,1875 870,1875 898,1922 870,1968 812,1968 788,1922"/>
      <polygon points="102,2048 163,2048 195,2112 163,2172 102,2172 62,2112"/>
      <polygon points="984,2120 1016,2120 1034,2149 1016,2178 984,2178 968,2149"/>
    </g>
  </svg>

  <section>
    <svg class="abs" style="left:205px;top:1198px;" width="165" height="155" viewBox="0 0 165 155">
      <polygon points="45,10 120,10 155,77 120,145 45,145 10,77" fill="var(--badge-blue)" stroke="var(--badge-blue)" stroke-width="20" stroke-linejoin="round"/>
    </svg>
    <div class="abs badge-num" style="left:255px;top:1224px;">1.</div>
    <h3 class="abs fence-title" style="left:148px;top:1375px;">Wooden Fence</h3>
    <div class="abs wood-art" role="img" aria-label="Illustration of a rustic wooden picket fence"></div>
    <svg class="abs" style="left:614px;top:1380px;" width="444" height="40" viewBox="0 0 444 40">
      <polyline points="0,38 274,38 274,3 336,3 336,14 364,14 364,21 444,21" fill="none" stroke="#2f9a5a" stroke-width="2" stroke-dasharray="2 3"/>
    </svg>
  </section>

  <section>
    <div class="abs gate-art" role="img" aria-label="Illustration of a black ornamental metal fence with gate"></div>
    <svg class="abs" style="left:136px;top:1818px;" width="508" height="38" viewBox="0 0 508 38">
      <polyline points="0,16 60,16 60,33 90,33 90,3 234,3 234,34 508,34" fill="none" stroke="var(--badge-blue)" stroke-width="2" stroke-dasharray="2 3"/>
    </svg>
    <svg class="abs" style="left:828px;top:1583px;" width="165" height="155" viewBox="0 0 165 155">
      <polygon points="45,10 120,10 155,77 120,145 45,145 10,77" fill="var(--badge-orange)" stroke="var(--badge-orange)" stroke-width="20" stroke-linejoin="round"/>
    </svg>
    <div class="abs badge-num" style="left:868px;top:1608px;">3.</div>
    <h3 class="abs fence-title" style="left:677px;top:1760px;">Aluminum Fence</h3>
  </section>

  <section>
    <svg class="abs" style="left:176px;top:2008px;" width="165" height="155" viewBox="0 0 165 155">
      <polygon points="45,10 120,10 155,77 120,145 45,145 10,77" fill="var(--badge-brown)" stroke="var(--badge-brown)" stroke-width="20" stroke-linejoin="round"/>
    </svg>
    <div class="abs badge-num" style="left:216px;top:2033px;">3.</div>
    <h3 class="abs fence-title" style="left:375px;top:2058px;">Trash Enclosure</h3>
    <div class="abs picket-art" role="img" aria-label="Illustration of a brown picket fence with climbing vine"></div>
    <svg class="abs" style="left:860px;top:2205px;" width="34" height="4" viewBox="0 0 34 4">
      <line x1="0" y1="2" x2="34" y2="2" stroke="var(--badge-blue)" stroke-width="2" stroke-dasharray="2 3"/>
    </svg>
  </section>
</main>

</body>
</html>
```